Reaching the Root: Reason in Clinical Choice-Making

I'd like a cover that looks like it would fit on the shelf next to "The Illness Illusion" by Conrad Meltby, "The Close of Forgetting" by Hugh Falkner, "Meal Mend" by Paul Ostrick, "The Energy Restart Plan" by Victor Pemberly or "The Gland Restart Plan" by the same or "The Cortex Restart Plan" by the same ... either text only (with some interesting fonts that make the title stand out, and the subtitle smaller) or a relevant image, though I'm not entirely sure what that would be since this is a book about big-picture medical decision making.
Author name is Dr Miriam Calloway, NMD
I'll eventually request an e-book, paperback, and audio cover from the winner...

Target Market(s)

practicing physicians

Industry/Entity Type

medicine

Requirements
Must have
• look similar to other books in the genre

```html
<!DOCTYPE html>
<html lang="en">
<head>
<meta charset="utf-8">
<title>Reaching the Root — Book Cover</title>
<link rel="stylesheet" href="https://fonts.googleapis.com/css2?family=Crimson+Text:ital,wght@0,400;0,600;1,400&family=EB+Garamond:wght@400;500&display=swap">
<style>
  :root {
    --backdrop: #02060a;
    --paper: #f4f4f4;
    --ink: #0a0a0a;
    --ink-soft: #555555;
    --leaf: #98bb3e;
    --leaf-dark: #6e8f3c;
  }
  html, body {
    margin: 0;
    padding: 0;
    width: 1200px;
    height: 1200px;
    overflow: hidden;
    background: var(--backdrop);
  }
  .canvas {
    width: 1200px;
    height: 1200px;
    display: block;
  }
  .cover-paper { fill: var(--paper); }
  .author-band { fill: var(--leaf); }
  .endorsement {
    font-family: "EB Garamond", serif;
    fill: var(--ink-soft);
    font-size: 21px;
    text-anchor: middle;
  }
  .endorsement-credit {
    font-family: "EB Garamond", serif;
    fill: var(--ink-soft);
    font-size: 14px;
    text-anchor: middle;
    letter-spacing: 0.3px;
  }
  .endorsement-credit .book-ref { font-style: italic; font-family: "Crimson Text", serif; }
  .title-dark {
    font-family: "Crimson Text", serif;
    fill: var(--ink);
    text-anchor: middle;
  }
  .title-accent {
    font-family: "Crimson Text", serif;
    fill: var(--leaf);
    text-anchor: middle;
  }
  .subtitle {
    font-family: "EB Garamond", serif;
    fill: #1f1f1f;
    font-size: 42px;
    text-anchor: middle;
  }
  .author-name {
    font-family: "Crimson Text", serif;
    font-weight: 600;
    fill: var(--ink);
    font-size: 54px;
    text-anchor: middle;
  }
  .rule-short { stroke: var(--leaf); stroke-width: 1.2; }
  .rule-long { stroke: var(--leaf-dark); stroke-width: 1.4; }
</style>
</head>
<body>
<svg class="canvas" viewBox="0 0 1200 1200" xmlns="http://www.w3.org/2000/svg" role="img" aria-label="Book cover: Reaching the Root, Reason in Clinical Choice-Making, by Dr Miriam Calloway, NMD">
  <defs>
    <linearGradient id="fadeRule" x1="0" x2="1" y1="0" y2="0">
      <stop offset="0" stop-color="#6e8f3c" stop-opacity="0"/>
      <stop offset="0.15" stop-color="#6e8f3c" stop-opacity="1"/>
      <stop offset="0.85" stop-color="#6e8f3c" stop-opacity="1"/>
      <stop offset="1" stop-color="#6e8f3c" stop-opacity="0"/>
    </linearGradient>
  </defs>

  <rect class="cover-paper" x="273" y="109" width="654" height="982"/>

  <g class="endorsement-block">
    <text class="endorsement" x="600" y="192">“A thoughtful framework for clarity in a world</text>
    <text class="endorsement" x="600" y="217">of complex medical decisions.”</text>
    <text class="endorsement-credit" x="600" y="241">-HUGH FALKNER, MD, author of <tspan class="book-ref">The Close of Forgetting</tspan></text>
    <line class="rule-short" x1="511" y1="263.5" x2="689" y2="263.5"/>
  </g>

  <g class="title-block">
    <text class="title-dark" x="600" y="437" font-size="158" textLength="510" lengthAdjust="spacingAndGlyphs">Reaching</text>
    <text class="title-dark" x="600" y="568" font-size="158">the</text>
    <text class="title-accent" x="610" y="742" font-size="198" textLength="516" lengthAdjust="spacingAndGlyphs">ROOT</text>
  </g>

  <g class="subtitle-block">
    <line x1="351" y1="792" x2="862" y2="792" stroke="url(#fadeRule)" stroke-width="1.6"/>
    <text class="subtitle" x="607" y="848" textLength="500" lengthAdjust="spacing">REASON IN CLINICAL</text>
    <text class="subtitle" x="607" y="892" textLength="490" lengthAdjust="spacing">CHOICE-MAKING</text>
    <line x1="351" y1="916" x2="862" y2="916" stroke="url(#fadeRule)" stroke-width="1.6"/>
  </g>

  <rect class="author-band" x="273" y="977" width="654" height="114"/>
  <text class="author-name" x="600" y="1046" textLength="566" lengthAdjust="spacingAndGlyphs">Dr Miriam Calloway, NMD</text>
</svg>
</body>
</html>
```